Erstellen einer animierten PowerPoint-Präsentation
Zielgruppe
Ex-Geheimagent Jens Kowalke hält Vorträge und gibt Trainings zum Thema Menschenkenntnis.
Aufgabenstellung
Die beigefügte PowerPoint-Präsentation soll an die bestehende Jens-Kowalke-CI (Siehe Beispiele) angepasst werden. Wichtig sind dezente Animationen.
Weil das Briefing offensichtlich nicht kar genug war: Mir geht es darum eine (1) neue PPT-Präsentation zu entwickeln, die an die CI der Beispieldokumente angepasst ist. Die beigefügte PPT-Präsentation dient als technische Vorlage für die benötigten Folien & Animationen. Rückfragen sind jederzeit erwünscht.

```html
<!DOCTYPE html>
<html lang="de">
<head>
<meta charset="utf-8">
<title>Präsentationsvorlage – Folienübersicht</title>
<link rel="stylesheet" href="https://fonts.googleapis.com/css2?family=Roboto+Condensed:wght@400;700;900&family=Arimo:wght@400;700&display=swap">
<style>
  :root{
    --red:#ed1c2e;
    --blue:#0088c7;
    --ink:#111;
    --paper:#fff;
    --grey:#e6e6e6;
    --head:"Roboto Condensed", "Arial Narrow", sans-serif;
    --body:"Arimo", Arial, sans-serif;
  }
  *{margin:0;padding:0;box-sizing:border-box}
  html,body{width:822px;height:1200px;overflow:hidden;background:var(--paper)}
  body{position:relative;font-family:var(--body);color:var(--ink)}
  .slide{position:absolute;width:364px;height:205px;background:var(--paper);overflow:hidden;
    box-shadow:0 2px 6px rgba(0,0,0,.18);--accent:var(--red)}
  .slide.is-blue{--accent:var(--blue)}
  .col-left{left:36px}.col-right{left:423px}
  .row-1{top:37px}.row-2{top:268px}.row-3{top:498px}.row-4{top:729px}.row-5{top:959px}
  .band{position:absolute;left:0;top:0;bottom:0;width:33px;background:var(--accent)}
  .edge{position:absolute;right:4px;top:0;bottom:0;border-left:1px dashed var(--accent)}
  .brand{position:absolute;top:12px;right:12px;font-family:var(--head);font-weight:900;
    font-size:9px;letter-spacing:.3px;color:var(--accent)}
  .plus{position:absolute;font-family:var(--body);font-size:13px;line-height:12px;color:var(--accent)}
  .plus span{display:block}
  .plus.left{left:42px;bottom:10px}
  .plus.left-title{left:56px;bottom:10px}
  .plus.right{right:10px;bottom:10px}
  .title{position:absolute;left:57px;font-family:var(--head)}
  .title h2{font-weight:900;font-size:25px;line-height:23px}
  .title p{font-weight:400;font-size:19px;line-height:19px}
  .center-title{position:absolute;left:33px;right:0;text-align:center;font-family:var(--head);
    font-size:16px;font-weight:400}
  .center-title b{font-weight:700}
  .tiny{font-size:4.4px;line-height:5.5px;color:#222}
  .tiny-title{font-size:4.6px;font-weight:700;margin-bottom:3px}

  /* Folie 1 */
  .cover-photo{position:absolute;left:220px;top:0;width:144px;height:205px;
    background:linear-gradient(135deg,#0e1a1c,#2b4a4c 60%,#0a0f10);border-radius:60px 0 0 0}
  .cover-brand{position:absolute;left:190px;top:80px;font-family:var(--head);font-weight:900;
    font-size:24px;color:var(--red)}

  /* Folie 2 */
  .steps{position:absolute;left:55px;top:94px;display:flex}
  .step{width:42px;height:34px;margin-right:-1px;background:var(--red);color:#fff;
    font-family:var(--head);font-weight:700;font-size:16px;display:flex;align-items:center;justify-content:center;
    clip-path:polygon(0 0,78% 0,100% 50%,78% 100%,0 100%,22% 50%)}
  .step:first-child{clip-path:polygon(0 0,78% 0,100% 50%,78% 100%,0 100%)}
  .step-texts{position:absolute;left:55px;top:139px;display:flex;gap:3px}
  .step-texts div{width:39px}

  /* Folie 3 */
  .avatars{position:absolute;left:71px;top:68px;display:flex;gap:8px}
  .avatars div{width:35px;height:35px;border-radius:50%;background:radial-gradient(circle at 40% 35%,#ccc,#555)}
  .profile-title{position:absolute;right:215px;top:110px;text-align:right;font-family:var(--head)}
  .profile-title h2{font-weight:900;font-size:25px;line-height:23px}
  .profile-title p{font-size:19px;line-height:19px}
  .profile-text{position:absolute;left:166px;top:67px;width:142px}
  .profile-text .lead{font-size:5.6px;line-height:7px;font-weight:700;margin-bottom:6px}
  .profile-text .tiny{margin-bottom:5px}

  /* Folie 4 */
  .cards{position:absolute;left:55px;top:80px;display:flex;gap:11px}
  .card{position:relative;width:63px;height:105px;border:1.5px solid var(--red);padding:18px 5px 0 5px}
  .card .num{position:absolute;right:-2px;top:6px;font-family:var(--head);font-weight:700;font-size:17px;color:var(--red);background:var(--paper);padding:0 1px}
  .card .tiny{font-size:3.9px;line-height:5.4px}

  /* Folie 5 */
  .list{position:absolute;left:56px;top:84px;list-style:none;width:220px}
  .list li{display:flex;align-items:flex-start;gap:5px;height:19px}
  .list .n{font-size:9px;font-weight:400;width:6px}
  .list .tiny{font-size:3.9px;line-height:5.4px}

  /* Folie 6 / 8 */
  .cycle{position:absolute;left:150px;top:76px}
  .cycle-label{position:absolute;font-size:6.3px;line-height:7.5px}
  .cycle-label b{color:var(--accent);font-weight:700}
  .cycle-label::before{content:"";display:block;width:28px;border-top:1px dashed var(--accent);margin-bottom:7px}
  .cycle-label.l{left:85px}
  .cycle-label.r{right:62px;text-align:right}
  .cycle-label.r::before{margin-left:auto}

  /* Folie 7 / 9 */
  .chat-title{position:absolute;left:56px;top:67px;font-family:var(--head)}
  .chat-title h2{font-weight:900;font-size:25px;line-height:23px}
  .chat-title p{font-size:19px;line-height:19px}
  .quote{position:absolute;left:56px;top:119px;font-size:5.6px;line-height:7px;width:130px}
  .media-placeholder{position:absolute;border-radius:6px;
    background:linear-gradient(160deg,#3a3a3a,#8a8a8a 70%,#c9c9c9)}
  .media-placeholder.chat{left:215px;top:78px;width:112px;height:118px}
  .media-placeholder.fact{left:215px;top:64px;width:132px;height:92px;
    background:linear-gradient(160deg,#f04a4a,#b52a36 55%,#17323b)}

  /* Folie 10 */
  .gauge{position:absolute;left:0;top:0}
</style>
</head>
<body>

<!-- Titel -->
<section class="slide col-left row-1">
  <div class="band"></div>
  <div class="cover-photo" role="img" aria-label="Porträtfoto des Referenten, der auf den Betrachter zeigt, vor dunklem Hintergrund"></div>
  <div class="cover-brand">KLARBLICK</div>
  <div class="edge"></div>
  <div class="title" style="top:78px"><h2>Headline</h2><p>Subline</p></div>
  <div class="plus" style="left:56px;top:133px"><span>+</span><span>+</span><span>+</span></div>
</section>

<!-- Ablauf in Schritten -->
<section class="slide col-right row-1">
  <div class="band"></div><div class="edge"></div>
  <div class="brand">KLARBLICK</div>
  <div class="title" style="top:35px"><h2>Headline</h2><p>Subline</p></div>
  <div class="steps">
    <div class="step">01</div><div class="step">02</div><div class="step">03</div><div class="step">04</div><div class="step">05</div>
  </div>
  <div class="step-texts">
    <div class="tiny"><div class="tiny-title">TITLE</div>Lorem ipsum dolor sit amet, consectetuer adipiscing Lorem ipsum dolor sit amet,</div>
    <div class="tiny"><div class="tiny-title">TITLE</div>Lorem ipsum dolor sit amet, consectetuer adipiscing Lorem ipsum dolor sit amet,</div>
    <div class="tiny"><div class="tiny-title">TITLE</div>Lorem ipsum dolor sit amet, consectetuer adipiscing Lorem ipsum dolor sit amet,</div>
    <div class="tiny"><div class="tiny-title">TITLE</div>Lorem ipsum dolor sit amet, consectetuer adipiscing Lorem ipsum dolor sit amet,</div>
    <div class="tiny"><div class="tiny-title">TITLE</div>Lorem ipsum dolor sit amet, consectetuer adipiscing Lorem ipsum dolor sit amet,</div>
  </div>
  <div class="plus right"><span>+</span><span>+</span><span>+</span></div>
</section>

<!-- Profil -->
<section class="slide col-left row-2">
  <div class="band"></div><div class="edge"></div>
  <div class="brand">KLARBLICK</div>
  <div class="avatars"><div role="img" aria-label="Profilbild Person 1"></div><div role="img" aria-label="Profilbild Person 2"></div></div>
  <div class="profile-title"><h2>Headline</h2><p>Subline</p></div>
  <div class="profile-text">
    <p class="lead">Lorem ipsum dolor sit amet, consectetuer adipiscing elit, sed diam nonummy nibh euismod tin</p>
    <p class="tiny">Lorem ipsum dolor sit amet, consectetuer adipiscing elit, sed diam nonummy nibh euismod tincidunt ut laoreet dolore magna aliquam erat volutpat. Ut wisi enim ad minim veniam, quis nostrud exerci tation</p>
    <p class="tiny">Lorem ipsum dolor sit amet, consectetuer adipiscing elit, sed diam nonummy nibh euismod tincidunt ut laoreet dolore magna aliquam erat volutpat. Ut wisi enim ad minim veniam, quis nostrud exerci tation Lorem ipsum dolor sit amet, consectetuer adipiscing elit, sed diam nonummy nibh euismod tincidunt ut laoreet dolore magna aliquam erat volutpat. Ut wisi enim ad minim veniam, quis nostrud exerci tation ullamcorper suscipit lobortis nisl ut aliquip ex ea commodo consequat. Duis autem vel eum iriure dolor in hendrerit in vulputate velit esse mo-</p>
  </div>
  <div class="plus right"><span>+</span><span>+</span><span>+</span></div>
</section>

<!-- Vier Karten -->
<section class="slide col-right row-2">
  <div class="band"></div><div class="edge"></div>
  <div class="brand">KLARBLICK</div>
  <div class="title" style="top:25px"><h2>Headline</h2><p>Subline</p></div>
  <div class="cards">
    <div class="card"><span class="num">01</span><div class="tiny-title">TITLE</div><p class="tiny">Lorem ipsum dolor sit amet, consectetuer adipiscing elit, sed diam nonummy nibh euismod tincidunt ut laoreet dolore magna aliquam erat volutpat. Ut wisi enim ad minim veniam, quis nostrud exerci tation ullamcorper suscipit lobortis nisl ut aliquip ex ea commodo consequat. Duis</p></div>
    <div class="card"><span class="num">02</span><div class="tiny-title">TITLE</div><p class="tiny">Lorem ipsum dolor sit amet, consectetuer adipiscing elit, sed diam nonummy nibh euismod tincidunt ut laoreet dolore magna aliquam erat volutpat. Ut wisi enim ad minim veniam, quis nostrud exerci tation ullamcorper suscipit lobortis nisl ut aliquip ex ea commodo consequat. Duis</p></div>
    <div class="card"><span class="num">03</span><div class="tiny-title">TITLE</div><p class="tiny">Lorem ipsum dolor sit amet, consectetuer adipiscing elit, sed diam nonummy nibh euismod tincidunt ut laoreet dolore magna aliquam erat volutpat. Ut wisi enim ad minim veniam, quis nostrud exerci tation ullamcorper suscipit lobortis nisl ut aliquip ex ea commodo consequat. Duis</p></div>
    <div class="card"><span class="num">04</span><div class="tiny-title">TITLE</div><p class="tiny">Lorem ipsum dolor sit amet, consectetuer adipiscing elit, sed diam nonummy nibh euismod tincidunt ut laoreet dolore magna aliquam erat volutpat. Ut wisi enim ad minim veniam, quis nostrud exerci tation ullamcorper suscipit lobortis nisl ut aliquip ex ea commodo consequat. Duis</p></div>
  </div>
  <div class="plus left"><span>+</span><span>+</span><span>+</span></div>
</section>

<!-- Nummerierte Liste -->
<section class="slide col-left row-3">
  <div class="band"></div><div class="edge"></div>
  <div class="brand">KLARBLICK</div>
  <div class="title" style="top:24px"><h2>Headline</h2><p>Subline</p></div>
  <ol class="list">
    <li><span class="n">1</span><span class="tiny">Lorem ipsum dolor sit amet, consectetuer adipiscing elit, sed diam nonummy nibh euismod tincidunt ut laoreet dolore magna aliquam erat volutpat. Ut wisi enim ad minim veniam, quis nostrud exerci tation</span></li>
    <li><span class="n">2</span><span class="tiny">Lorem ipsum dolor sit amet, consectetuer adipiscing elit, sed diam nonummy nibh euismod tincidunt ut laoreet dolore magna aliquam erat volutpat. Ut wisi enim ad minim veniam, quis nostrud exerci tation</span></li>
    <li><span class="n">3</span><span class="tiny">Lorem ipsum dolor sit amet, consectetuer adipiscing elit, sed diam nonummy nibh euismod tincidunt ut laoreet dolore magna aliquam erat volutpat. Ut wisi enim ad minim veniam, quis nostrud exerci tation</span></li>
    <li><span class="n">4</span><span class="tiny">Lorem ipsum dolor sit amet, consectetuer adipiscing elit, sed diam nonummy nibh euismod tincidunt ut laoreet dolore magna aliquam erat volutpat. Ut wisi enim ad minim veniam, quis nostrud exerci tation</span></li>
    <li><span class="n">5</span><span class="tiny">Lorem ipsum dolor sit amet, consectetuer adipiscing elit, sed diam nonummy nibh euismod tincidunt ut laoreet dolore magna aliquam erat volutpat. Ut wisi enim ad minim veniam, quis nostrud exerci tation</span></li>
  </ol>
  <div class="plus right"><span>+</span><span>+</span><span>+</span></div>
</section>

<!-- Kreislauf des Vertrauens -->
<section class="slide col-right row-3">
  <div class="band"></div><div class="edge"></div>
  <div class="brand">KLARBLICK</div>
  <h2 class="center-title" style="top:40px">Kreislauf des <b>Vertrauens</b></h2>
  <svg class="cycle" width="86" height="86" viewBox="0 0 86 86" aria-hidden="true">
    <defs><path id="ringPathA" d="M43 10 A33 33 0 1 1 42.9 10"/></defs>
    <circle cx="43" cy="43" r="33" fill="none" stroke="var(--red)" stroke-width="10"
      stroke-dasharray="48.8 3" transform="rotate(-87 43 43)"/>
    <text font-family="Arimo, sans-serif" font-size="4.2" fill="#fff">
      <textPath href="#ringPathA" startOffset="5">Schritt 1</textPath>
      <textPath href="#ringPathA" startOffset="57">Schritt 2</textPath>
      <textPath href="#ringPathA" startOffset="109">Schritt 3</textPath>
      <textPath href="#ringPathA" startOffset="161">Schritt 4</textPath>
    </text>
    <text x="43" y="55" text-anchor="middle" font-family="Roboto Condensed, sans-serif" font-weight="900" font-size="34" fill="var(--red)">?</text>
  </svg>
  <p class="cycle-label l" style="top:81px">Der andere übernimmt<br><b>Verantwortung</b></p>
  <p class="cycle-label l" style="top:135px">Der andere spürt<br><b>Vertrauen</b></p>
  <p class="cycle-label r" style="top:81px">Ich<br><b>vertraue</b></p>
  <p class="cycle-label r" style="top:135px">Ich&nbsp; übertrage<br><b>Verantwortung</b></p>
  <div class="plus left"><span>+</span><span>+</span><span>+</span></div>
</section>

<!-- Chat-Aufgabe -->
<section class="slide col-left row-4">
  <div class="band"></div><div class="edge"></div>
  <div class="brand">KLARBLICK</div>
  <div class="chat-title"><h2>Notieren Sie</h2><p>bitte in den Chat</p></div>
  <p class="quote">„An welchen Merkmalen können wir erkennen, dass in unserem Team Vertrauen fehlt?“</p>
  <div class="media-placeholder chat" role="img" aria-label="Platz für Illustration: Hände halten ein Tablet mit einer Chat-Nachricht"></div>
  <div class="plus left-title"><span>+</span><span>+</span><span>+</span></div>
</section>

<!-- Kreislauf der Belanglosigkeit -->
<section class="slide col-right row-4 is-blue">
  <div class="band"></div><div class="edge"></div>
  <div class="brand">KLARBLICK</div>
  <h2 class="center-title" style="top:40px">Kreislauf der <b>Belanglosigkeit</b></h2>
  <svg class="cycle" width="86" height="86" viewBox="0 0 86 86" aria-hidden="true">
    <defs><path id="ringPathB" d="M43 10 A33 33 0 1 1 42.9 10"/></defs>
    <circle cx="43" cy="43" r="33" fill="none" stroke="var(--blue)" stroke-width="10"
      stroke-dasharray="48.8 3" transform="rotate(-87 43 43)"/>
    <text font-family="Arimo, sans-serif" font-size="4.2" fill="#fff">
      <textPath href="#ringPathB" startOffset="5">Schritt 1</textPath>
      <textPath href="#ringPathB" startOffset="57">Schritt 2</textPath>
      <textPath href="#ringPathB" startOffset="109">Schritt 3</textPath>
      <textPath href="#ringPathB" startOffset="161">Schritt 4</textPath>
    </text>
    <text x="43" y="55" text-anchor="middle" font-family="Roboto Condensed, sans-serif" font-weight="900" font-size="34" fill="var(--blue)">?</text>
  </svg>
  <p class="cycle-label l" style="top:81px">Der andere<br><b>vermeidet jedes<br>Risiko</b></p>
  <p class="cycle-label l" style="top:135px">Der andere spürt<br><b>kein Vertrauen</b></p>
  <p class="cycle-label r" style="top:81px">Ich habe<br><b>Bedenken</b></p>
  <p class="cycle-label r" style="top:135px">Ich<br><b>sichere mich ab</b></p>
  <div class="plus left"><span>+</span><span>+</span><span>+</span></div>
</section>

<!-- Beobachtbare Merkmale -->
<section class="slide col-left row-5">
  <div class="band"></div><div class="edge"></div>
  <div class="brand">KLARBLICK</div>
  <div class="chat-title"><h2>Beobachtbare</h2><p>Merkmale:</p></div>
  <p class="quote">„Woran können wir erkennen, dass in unserem Team Vertrauen fehlt?“</p>
  <div class="media-placeholder fact" role="img" aria-label="Platz für Grafik mit zwei Sprechblasen: Did You Know?"></div>
  <div class="plus left-title"><span>+</span><span>+</span><span>+</span></div>
</section>

<!-- Vertrauen vs. Belanglosigkeit -->
<section class="slide col-right row-5">
  <div class="band"></div><div class="edge"></div>
  <div class="brand">KLARBLICK</div>
  <h2 class="center-title" style="top:34px">Vertrauen <b>vs. Belanglosigkeit</b></h2>
  <svg class="gauge" width="364" height="205" viewBox="0 0 364 205" aria-hidden="true">
    <path d="M100 165 A93 93 0 0 1 263.2 104 L236 127.6 A57 57 0 0 0 136 165 Z" fill="var(--red)"/>
    <path d="M263.2 104 A93 93 0 0 1 286 165 L250 165 A57 57 0 0 0 236 127.6 Z" fill="var(--grey)"/>
    <line x1="193" y1="68" x2="193" y2="113" stroke="#222" stroke-width=".8" stroke-dasharray="2 1.5"/>
    <line x1="98" y1="166" x2="140" y2="166" stroke="#222" stroke-width=".8" stroke-dasharray="2 1.5"/>
    <line x1="246" y1="166" x2="288" y2="166" stroke="#222" stroke-width=".8" stroke-dasharray="2 1.5"/>
    <line x1="189" y1="168" x2="256" y2="110" stroke="#2b2b2b" stroke-width="6" stroke-linecap="round"/>
    <circle cx="189" cy="168" r="5" fill="#2b2b2b"/>
    <g font-family="Arimo, sans-serif" font-size="4.2" text-anchor="middle">
      <text x="193" y="119" font-weight="700">mittlere</text>
      <text x="193" y="124" font-weight="700">Ausprägung</text>
      <text x="119" y="153" fill="#fff">Kein</text>
      <text x="119" y="158" fill="#fff">Vertrauen</text>
      <text x="267" y="153">Volles</text>
      <text x="267" y="158">Vertrauen</text>
      <text x="119" y="173" font-weight="700">zu geringe</text>
      <text x="119" y="178" font-weight="700">Ausprägung</text>
      <text x="267" y="173" font-weight="700">zu hohe</text>
      <text x="267" y="178" font-weight="700">Ausprägung</text>
    </g>
  </svg>
  <div class="plus right"><span>+</span><span>+</span><span>+</span></div>
</section>

</body>
</html>
```